Visitenkarten-Design für Pflegedienst
Zielgruppe
Pflegedienst
Aufgabenstellung
Siehe Beispielvisitenkarte. Es soll so ähnlich designt werden mit hochwertigem Papier. Die Angaben darauf sind auch schon korrekt.

```html
<!DOCTYPE html>
<html lang="de">
<head>
<meta charset="utf-8">
<title>Visitenkarte Sonnbruck Pflege</title>
<link href="https://fonts.googleapis.com/css2?family=Montserrat:wght@400;500;600&display=swap" rel="stylesheet">
<style>
:root{
  --bg:#dadada;
  --card:#ffffff;
  --blue:#33558b;
  --red:#d41317;
  --ink:#1c1c1c;
  --muted:#555555;
}
*{margin:0;padding:0;box-sizing:border-box}
html,body{width:1200px;height:885px;overflow:hidden;background:var(--bg)}
body{position:relative;font-family:"Montserrat",Arial,sans-serif;color:var(--ink)}
.card{position:absolute;top:303px;width:432px;height:280px;background:var(--card);overflow:hidden}
.card--front{left:103px}
.card--back{left:657px}
.icon{position:absolute;left:17px;width:13px;height:13px}
.line{position:absolute;left:41px;font-size:12.5px;line-height:1;white-space:nowrap}
.person-name{position:absolute;left:41px;top:55px;font-size:15px;font-weight:500;letter-spacing:.2px}
.person-role{position:absolute;left:41px;top:75px;font-size:11px}
.company{font-weight:600}
.portrait{position:absolute;left:257px;top:64px;width:152px;height:152px;border-radius:50%;border:3.5px solid var(--blue);padding:3px;background:var(--card)}
.portrait__fill{width:100%;height:100%;border-radius:50%;background:radial-gradient(circle at 50% 40%,#c99a7e 0%,#a97a62 25%,#eeeeee 55%,#ffffff 80%)}
.bars{position:absolute;left:0;bottom:0}
.brand{position:absolute;left:0;width:432px;top:108px;display:flex;align-items:center;justify-content:center;gap:14px}
.brand-mark{width:34px;height:34px;border-radius:50%;background:var(--blue);flex:none}
.brand-name{font-size:22px;font-weight:500;color:var(--blue);white-space:nowrap}
.brand-tagline{position:absolute;left:0;width:432px;top:152px;text-align:center;font-size:11.5px;color:var(--muted);white-space:nowrap;letter-spacing:1.5px}
.web-tab{position:absolute;left:0;bottom:0}
.web-url{position:absolute;left:0;width:432px;top:241px;text-align:center;color:#fff;font-size:13.5px;letter-spacing:.2px}
</style>
</head>
<body>

<section class="card card--front">
  <svg class="icon" style="top:58px" viewBox="0 0 13 13"><circle cx="6.5" cy="6.5" r="6.5" fill="var(--blue)"/><circle cx="6.5" cy="5" r="2" fill="#fff"/><path d="M3.3 10a3.4 3 0 0 1 6.4 0z" fill="#fff"/></svg>
  <div class="person-name">DARIAN WELLMER LL.M.</div>
  <div class="person-role">Wirtschaftsjurist - Geschäftsführer</div>

  <div class="line company" style="top:129px">Sonnbruck Pflege GmbH</div>
  <svg class="icon" style="top:143px" viewBox="0 0 13 13"><circle cx="6.5" cy="6.5" r="6.5" fill="var(--blue)"/><path d="M6.5 2.8a2.6 2.6 0 0 1 2.6 2.6c0 2-2.6 4.8-2.6 4.8S3.9 7.4 3.9 5.4A2.6 2.6 0 0 1 6.5 2.8z" fill="#fff"/><circle cx="6.5" cy="5.4" r="1" fill="var(--blue)"/></svg>
  <div class="line" style="top:144px">Lindenhofer Str. 18</div>
  <div class="line" style="top:159px">71234 Felsingen</div>

  <svg class="icon" style="top:188px" viewBox="0 0 13 13"><circle cx="6.5" cy="6.5" r="6.5" fill="var(--blue)"/><rect x="4.4" y="3" width="4.2" height="7" rx="0.8" fill="#fff"/></svg>
  <div class="line" style="top:189px">+49 151 20483917</div>
  <svg class="icon" style="top:203px" viewBox="0 0 13 13"><circle cx="6.5" cy="6.5" r="6.5" fill="var(--blue)"/><path d="M4 3.4l1.5-.4 1 2-1 .8a5 5 0 0 0 2 2l.8-1 2 1-.4 1.5c-3 .4-6.3-2.9-5.9-5.9z" fill="#fff"/></svg>
  <div class="line" style="top:204px">+49 7031 5528400</div>
  <svg class="icon" style="top:218px" viewBox="0 0 13 13"><circle cx="6.5" cy="6.5" r="6.5" fill="var(--blue)"/><rect x="3.5" y="5" width="6" height="4.2" rx=".6" fill="#fff"/><rect x="4.6" y="3" width="3.8" height="2.4" fill="#fff"/></svg>
  <div class="line" style="top:219px">+49 7031 5528402</div>
  <svg class="icon" style="top:233px" viewBox="0 0 13 13"><circle cx="6.5" cy="6.5" r="6.5" fill="var(--blue)"/><rect x="3.3" y="4.3" width="6.4" height="4.4" rx=".5" fill="#fff"/><path d="M3.5 4.6l3 2.2 3-2.2" stroke="var(--blue)" stroke-width=".8" fill="none"/></svg>
  <div class="line" style="top:234px">dw@sonnbruck-pflege.de</div>

  <div class="portrait"><div class="portrait__fill" role="img" aria-label="Porträtfoto des Geschäftsführers"></div></div>

  <svg class="bars" width="432" height="22" viewBox="0 0 432 22">
    <polygon points="0,9 249,9 238,22 0,22" fill="var(--red)"/>
    <polygon points="266,0 432,0 432,22 246,22" fill="var(--blue)"/>
  </svg>
</section>

<section class="card card--back">
  <div class="brand">
    <div class="brand-mark"></div>
    <div class="brand-name">Sonnbruck Pflege GmbH</div>
  </div>
  <div class="brand-tagline">Außerklinische Intensivpflege</div>

  <svg class="web-tab" width="432" height="58" viewBox="0 0 432 58">
    <path d="M0 33 H105 Q117 33 117 22 V16 Q117 0 133 0 H300 Q316 0 316 16 V22 Q316 33 328 33 H432 V58 H0 Z" fill="var(--blue)"/>
  </svg>
  <div class="web-url">www.sonnbruck-pflege.de</div>
</section>

</body>
</html>
```